Business card for a yoga studio
The Reed Yoga Studio
Project: Business card for a yoga studio
Business card for a yoga studio - Health
Creative Brief
Bright & Fun-filled
Lorna Pichet
Owner
27316 Hollin Avenue, Suite 408 Dallas, TX 75219
972-318-YOGA(9642)
lorna@thereedyogastudio.example
TheReedYogaStudio.example
Would like a new/fresh business card design since we have moved. Don't like the dark/heavy feel of the existing card. I would like the phone number to appear as: 972-318-YOGA(9642).
TheReedYogaStudio TheReedYogaStudio
Would like to avoid solid black background or solid dark color background due to the way the cards show wear easily in everyday use/transport, as well as fingerprints.

```html
<!DOCTYPE html>
<html lang="en">
<head>
<meta charset="utf-8">
<title>The Reed Yoga Studio – Business Card</title>
<link rel="stylesheet" href="https://fonts.googleapis.com/css2?family=Open+Sans:ital,wght@0,400;0,600;0,700;1,400&display=swap">
<style>
  :root {
    --ink: #2b2b2b;
    --ink-soft: #555555;
    --paper: #ffffff;
    --band: #f1f1f1;
    --backdrop: #d9d9d9;
    --rule: #2b2b2b;
    --back-paper: #f6f6f6;
    --figure-light: #ffffff;
    --figure-mid: #dedede;
  }
  * { margin: 0; padding: 0; box-sizing: border-box; }
  html, body {
    width: 1200px; height: 842px; overflow: hidden;
    background: var(--backdrop);
    font-family: "Open Sans", Arial, sans-serif;
  }
  .canvas { position: relative; width: 1200px; height: 842px; }
  .card {
    position: absolute;
    width: 525px; height: 300px;
    top: 271px;
    box-shadow: 0 6px 18px rgba(0,0,0,.16);
    overflow: hidden;
  }

  /* Front */
  .card--front { left: 50px; background: var(--paper); }
  .brand {
    position: absolute; top: 40px; left: 0; right: 0;
    display: flex; align-items: center; justify-content: center; gap: 10px;
    color: var(--ink); font-size: 21px; font-weight: 400; letter-spacing: .5px;
  }
  .brand__dot { width: 14px; height: 14px; border-radius: 50%; background: var(--ink); }
  .info-band {
    position: absolute; left: 0; right: 0; top: 128px; height: 124px;
    background: var(--band); color: var(--ink);
    border-top: 2px solid var(--rule);
    border-bottom: 2px solid var(--rule);
  }
  .info-band__divider {
    position: absolute; left: 258px; top: 14px; bottom: 14px; width: 1px; background: var(--rule);
  }
  .person { position: absolute; left: 22px; top: 12px; width: 215px; }
  .person__name { font-size: 16px; font-weight: 700; line-height: 1.2; }
  .person__role { font-size: 12px; line-height: 1.4; color: var(--ink-soft); }
  .person__rule { height: 1px; background: var(--rule); margin: 7px 0 8px; }
  .person__address { font-size: 11.5px; line-height: 1.55; }
  .contact {
    position: absolute; left: 274px; top: 34px; list-style: none;
    font-size: 11.5px; line-height: 1.6;
  }
  .contact li { display: flex; align-items: center; gap: 7px; }
  .contact svg { width: 11px; height: 11px; flex: none; }

  /* Back */
  .card--back { left: 625px; background: var(--back-paper); border-top: 6px solid var(--ink); }
  .pose-figure {
    position: absolute; left: 268px; top: 36px; width: 185px; height: 108px;
    border-radius: 8px;
    background: radial-gradient(ellipse at center, var(--figure-light) 0%, var(--figure-mid) 100%);
  }
  .web-line {
    position: absolute; left: 60px; top: 200px;
    color: var(--ink); font-size: 17px; font-style: italic; letter-spacing: 2.4px;
  }
</style>
</head>
<body>
<main class="canvas">
  <section class="card card--front" aria-label="Card front">
    <div class="brand"><span class="brand__dot"></span><span>The Reed Yoga Studio</span></div>
    <div class="info-band">
      <div class="person">
        <p class="person__name">Lorna Pichet</p>
        <p class="person__role">Owner</p>
        <div class="person__rule"></div>
        <p class="person__address">27316 Hollin Avenue, Suite 408<br>Dallas, TX 75219</p>
      </div>
      <div class="info-band__divider"></div>
      <ul class="contact">
        <li>
          <svg viewBox="0 0 12 12" aria-hidden="true"><circle cx="6" cy="6" r="6" fill="#2b2b2b"/><path d="M4 3.2l1 1.2-.6.8c.5 1 1.2 1.7 2.2 2.2l.8-.6 1.2 1-.7 1C5.8 8.6 3.4 6.2 3.2 4z" fill="#fff"/></svg>
          972-318-YOGA(9642)
        </li>
        <li>
          <svg viewBox="0 0 12 12" aria-hidden="true"><circle cx="6" cy="6" r="6" fill="#2b2b2b"/><rect x="3" y="4" width="6" height="4.2" fill="none" stroke="#fff" stroke-width=".9"/><path d="M3 4l3 2.3L9 4" fill="none" stroke="#fff" stroke-width=".9"/></svg>
          lorna@thereedyogastudio.example
        </li>
        <li>
          <svg viewBox="0 0 12 12" aria-hidden="true"><circle cx="6" cy="6" r="6" fill="#2b2b2b"/><circle cx="6" cy="6" r="3.2" fill="none" stroke="#fff" stroke-width=".8"/><path d="M2.8 6h6.4M6 2.8c-1.6 2-1.6 4.4 0 6.4M6 2.8c1.6 2 1.6 4.4 0 6.4" fill="none" stroke="#fff" stroke-width=".7"/></svg>
          www.TheReedYogaStudio.example
        </li>
      </ul>
    </div>
  </section>

  <section class="card card--back" aria-label="Card back">
    <div class="pose-figure" role="img" aria-label="Silhouette of a person in a downward dog yoga pose"></div>
    <p class="web-line">www.TheReedYogaStudio.example</p>
  </section>
</main>
</body>
</html>
```